Business Card Design

We are a radiology group

We are working to move into new service centers

We want to communicate innovation and bringing our customers ahead with technology and outstanding results

I have uploaded a high resolution logo as requested :-)

Target Market(s)

hospitals, clinics

Industry/Entity Type

Business

Contact Information for Business Card

Linda R. Feathersby, MBA, CIIP
CTIO
linda.feathersby@trovexa-rad.com
cell 607-481-2937
www.trovexa-rad.com
Trovexa Radiology Partners, PC

```html
<!DOCTYPE html>
<html lang="en">
<head>
<meta charset="utf-8">
<title>Trovexa Radiology Partners – Business Card</title>
<link rel="stylesheet" href="https://fonts.googleapis.com/css2?family=Open+Sans:wght@400;600&display=swap">
<style>
  :root {
    --page-bg: #d6d6d6;
    --card-white: #ffffff;
    --band-blue: #8fd0ee;
    --band-blue-dark: #6cbde3;
    --panel-dark-top: #5c5c5c;
    --panel-dark-bottom: #3c3c3c;
    --accent-blue: #86c9ea;
    --text-light: #f2f2f2;
    --brand-grey: #4e4e4e;
  }
  * { margin: 0; padding: 0; box-sizing: border-box; }
  html, body {
    width: 1200px;
    height: 900px;
    overflow: hidden;
    background: var(--page-bg);
    font-family: "Open Sans", sans-serif;
  }
  .business-card {
    position: absolute;
    left: 150px;
    top: 193px;
    width: 900px;
    height: 514px;
    border-radius: 48px;
    overflow: hidden;
    background: var(--card-white);
    box-shadow: 0 18px 40px rgba(0,0,0,0.18);
  }
  .brand-area {
    position: absolute;
    left: 0; top: 0;
    width: 100%;
    height: 290px;
    background: var(--card-white);
  }
  .brand-name {
    position: absolute;
    left: 250px;
    top: 160px;
    font-size: 38px;
    font-weight: 600;
    letter-spacing: 1px;
    color: var(--brand-grey);
    white-space: nowrap;
  }
  .accent-band {
    position: absolute;
    left: 0; top: 290px;
    width: 100%;
    height: 16px;
    background: linear-gradient(to bottom, var(--band-blue), var(--band-blue-dark));
  }
  .contact-panel {
    position: absolute;
    left: 0; top: 306px;
    width: 100%;
    height: 208px;
  }
  .panel-texture {
    position: absolute;
    inset: 0;
    background: linear-gradient(to bottom, var(--panel-dark-top), var(--panel-dark-bottom));
  }
  .person-name {
    position: absolute;
    left: 58px;
    top: 28px;
    font-size: 30px;
    font-weight: 600;
    color: var(--accent-blue);
  }
  .person-credentials {
    position: absolute;
    left: 58px;
    top: 72px;
    font-size: 22px;
    color: var(--text-light);
  }
  .contact-list {
    position: absolute;
    left: 58px;
    top: 120px;
    list-style: none;
  }
  .contact-item {
    display: flex;
    align-items: center;
    height: 28px;
    font-size: 22px;
    color: var(--text-light);
  }
  .contact-icon {
    width: 22px;
    height: 22px;
    margin-right: 8px;
    flex: none;
  }
</style>
</head>
<body>
  <main class="business-card">
    <section class="brand-area">
      <div class="brand-name">Trovexa Radiology Partners</div>
    </section>

    <div class="accent-band"></div>

    <section class="contact-panel">
      <div class="panel-texture" role="img" aria-label="Dark grey perforated metal texture"></div>

      <h1 class="person-name">Linda R. Feathersby</h1>
      <p class="person-credentials">MBA, CIIP CTIO</p>

      <ul class="contact-list">
        <li class="contact-item">
          <svg class="contact-icon" viewBox="0 0 22 22" aria-hidden="true">
            <rect x="5" y="1" width="12" height="20" rx="2" fill="var(--accent-blue)"/>
            <rect x="7" y="4" width="8" height="6" fill="#3f3f3f"/>
            <rect x="7" y="12" width="2" height="2" fill="#3f3f3f"/>
            <rect x="10" y="12" width="2" height="2" fill="#3f3f3f"/>
            <rect x="13" y="12" width="2" height="2" fill="#3f3f3f"/>
            <rect x="7" y="16" width="2" height="2" fill="#3f3f3f"/>
            <rect x="10" y="16" width="2" height="2" fill="#3f3f3f"/>
            <rect x="13" y="16" width="2" height="2" fill="#3f3f3f"/>
          </svg>
          <span>607-481-2937</span>
        </li>
        <li class="contact-item">
          <svg class="contact-icon" viewBox="0 0 22 22" aria-hidden="true">
            <rect x="1" y="5" width="20" height="14" rx="1.5" fill="var(--accent-blue)"/>
            <path d="M1.5 6 L11 13 L20.5 6" fill="none" stroke="#3f3f3f" stroke-width="1.6"/>
          </svg>
          <span>www.trovexa-rad.com</span>
        </li>
        <li class="contact-item">
          <svg class="contact-icon" viewBox="0 0 22 22" aria-hidden="true">
            <circle cx="11" cy="11" r="9.5" fill="none" stroke="var(--accent-blue)" stroke-width="1.8"/>
            <ellipse cx="11" cy="11" rx="4" ry="9.5" fill="none" stroke="var(--accent-blue)" stroke-width="1.5"/>
            <line x1="1.5" y1="11" x2="20.5" y2="11" stroke="var(--accent-blue)" stroke-width="1.5"/>
            <line x1="3" y1="6.5" x2="19" y2="6.5" stroke="var(--accent-blue)" stroke-width="1.2"/>
            <line x1="3" y1="15.5" x2="19" y2="15.5" stroke="var(--accent-blue)" stroke-width="1.2"/>
          </svg>
          <span>linda.feathersby@trovexa-rad.com</span>
        </li>
      </ul>
    </section>
  </main>
</body>
</html>
```